Business card design needed

I need a business card for my new Food & Lifestyle Coaching business - "Bloomvale Food & Lifestlye Coaching"

i already have a logo and would like to have that incorporated into the business card, obviously.

i would like a design that says "fresh" and "funky" - my target market is female, aged 20-45 so i want something that will stand out to them when they see it.

My "Company Colour" is Apple Green
Updates

Thankyou to everyone who has submitted a design for my project. At this stage i have quite a large number of designs to chose from and with only a short time until my project closes i am focusing now on chosing from those i have already shortlisted so am unfortunately not considering any new desings.

Thankyou again for your interest in my project.

Target Market(s)

Female, Health Conscious (or looking to improve their health/lifestyle), aged between 20-45

Industry/Entity Type

Business

Contact Information for Business Card

Tamsin Corley
Ph: 0417382946
Email: eatwell@marovex.com

Requirements
Must have
• Must include my existing Logo
Nice to have
• Would be nice to incoirporate and appointment card on the back

```html
<!DOCTYPE html>
<html lang="en">
<head>
<meta charset="utf-8">
<title>Bloomvale Food &amp; Lifestlye Coaching – Business Card</title>
<link href="https://fonts.googleapis.com/css2?family=Montserrat:wght@300;400;700&display=swap" rel="stylesheet">
<style>
  :root {
    --backdrop: #303336;
    --apple-green: #8dc63f;
    --apple-green-light: #a9d86a;
    --forest-green-centre: #5b9528;
    --forest-green-edge: #234a05;
    --card-white: #ffffff;
    --petal-grey: #dfe0e2;
    --ink: #1e1e1e;
  }
  * { margin: 0; padding: 0; box-sizing: border-box; }
  html, body {
    width: 1200px;
    height: 1200px;
    overflow: hidden;
    background: var(--backdrop);
    font-family: "Montserrat", sans-serif;
  }
  .card {
    position: absolute;
    left: 160px;
    width: 880px;
    height: 503px;
    overflow: hidden;
    box-shadow: 0 6px 18px rgba(0,0,0,0.35);
  }
  .card--front { top: 80px; background: var(--apple-green); }
  .card--back {
    top: 617px;
    background: radial-gradient(ellipse at 50% 52%, var(--forest-green-centre) 0%, #3f7416 40%, var(--forest-green-edge) 85%);
  }
  .card__art { position: absolute; inset: 0; width: 100%; height: 100%; }

  .brand {
    position: absolute;
    color: var(--ink);
    font-weight: 400;
    line-height: 1;
  }
  .brand__name { display: block; font-size: 62px; letter-spacing: -1px; }
  .brand__tagline { display: block; font-size: 15px; margin-top: 8px; padding-left: 70px; }
  .card--front .brand { left: 70px; top: 130px; }
  .card--back .brand {
    color: var(--card-white);
    left: 0; right: 0; top: 170px;
    text-align: center;
  }
  .card--back .brand__name { font-size: 96px; }
  .card--back .brand__tagline { font-size: 22px; margin-top: 14px; padding-left: 120px; }

  .contact {
    position: absolute;
    right: 48px;
    top: 255px;
    text-align: right;
    color: var(--card-white);
  }
  .contact__name { font-size: 30px; font-weight: 700; margin-bottom: 8px; }
  .contact__line { font-size: 19px; font-weight: 300; line-height: 1.45; }
</style>
</head>
<body>

  <section class="card card--front" aria-label="Business card front">
    <svg class="card__art" viewBox="0 0 880 503" aria-hidden="false">
      <defs>
        <linearGradient id="petalShade" x1="0" y1="0" x2="1" y2="1">
          <stop offset="0" stop-color="#ffffff"/>
          <stop offset="0.55" stop-color="#f4f4f5"/>
          <stop offset="1" stop-color="var(--petal-grey)"/>
        </linearGradient>
      </defs>
      <path d="M0 0 H385 C440 80 470 200 450 320 L590 382 C520 432 430 470 330 503 H0 Z"
            fill="url(#petalShade)" stroke="var(--apple-green-light)" stroke-width="4"
            role="img" aria-label="Soft white and grey petal shapes"/>
    </svg>

    <div class="brand">
      <span class="brand__name">Bloomvale</span>
      <span class="brand__tagline">Food &amp; Lifestlye Coaching</span>
    </div>

    <div class="contact">
      <p class="contact__name">Tamsin Corley</p>
      <p class="contact__line">T: 0417382946</p>
      <p class="contact__line">E: eatwell@marovex.com</p>
    </div>
  </section>

  <section class="card card--back" aria-label="Business card back">
    <div class="brand">
      <span class="brand__name">Bloomvale</span>
      <span class="brand__tagline">Food &amp; Lifestlye Coaching</span>
    </div>
  </section>

</body>
</html>
```